Veltrona stationery design

Design stationery for us that fits with the colours of the logo. We are looking for letterheads, business cards etc. Something we can use for a prospectus and marketing presentations in power point. Must be completed in such a manner that it represents a corporate image for large enterprise clients and other large organisations. The company is a project assurance and monitoring company that works in all industries.

```html
<!DOCTYPE html>
<html lang="en">
<head>
<meta charset="utf-8">
<title>Veltrona Stationery</title>
<link rel="stylesheet" href="https://fonts.googleapis.com/css2?family=Poppins:wght@400;500;600;700&family=Allura&display=swap">
<style>
:root{
  --stage:#4a4a4a;
  --paper:#ffffff;
  --navy:#0d3789;
  --blue:#0a5fb0;
  --orange:#f57c00;
  --red:#e8200f;
  --ink:#1b1b1b;
  --label:#f2f2f2;
}
*{margin:0;padding:0;box-sizing:border-box}
html,body{width:1200px;height:3053px;overflow:hidden;background:var(--stage);font-family:"Poppins",sans-serif;color:var(--ink)}
.canvas{position:relative;width:1200px;height:3053px}
.sheet,.card{position:absolute;background:var(--paper);overflow:hidden;box-shadow:0 6px 22px rgba(0,0,0,.35)}
.abs{position:absolute}
.decor{position:absolute;left:0;top:0}

/* Letterhead */
.letterhead{left:130px;top:120px;width:941px;height:1330px}
.brand{font-weight:700;color:var(--navy);letter-spacing:1px;display:flex;align-items:center;gap:12px}
.brand-mark{display:inline-block;background:var(--orange);border-radius:50%}
.letterhead .brand{left:55px;top:72px;font-size:32px}
.letterhead .brand-mark{width:40px;height:40px}
.recipient{left:75px;top:205px}
.recipient .to{font-size:28px;line-height:36px}
.recipient .name{font-size:37px;font-weight:700;color:var(--navy);line-height:50px}
.recipient .role{font-size:23px;line-height:34px}
.contact-box{left:638px;top:212px;display:flex;gap:10px}
.contact-box .keys{width:26px;height:100px;border:1.5px solid var(--orange);border-radius:13px;display:flex;flex-direction:column;justify-content:space-around;align-items:center;font-size:12px}
.contact-box .vals{font-size:13px;line-height:16px;display:flex;flex-direction:column;justify-content:space-between;padding:3px 0}
.subject{left:75px;top:392px;font-size:21px}
.subject b{color:var(--orange);font-weight:600}
.body{left:75px;top:468px;width:790px;font-size:17.6px;line-height:21px;text-align:justify}
.body p{margin-bottom:21px}
.signoff{left:75px;top:965px}
.signoff .script{font-family:"Allura",cursive;font-size:40px;line-height:44px}
.signoff .name{font-size:31px;font-weight:700;line-height:40px}
.signoff .role{font-size:18px}
.date{left:755px;top:1024px;font-size:20px;font-weight:700}
.contact-row{left:75px;top:1152px;display:flex;gap:24px;font-size:18px;align-items:center}
.contact-row span{display:flex;align-items:center;gap:12px}
.icon{width:30px;height:30px;border-radius:50%;background:var(--navy);display:inline-flex;align-items:center;justify-content:center}

/* Labels */
.label{position:absolute;left:0;width:1200px;text-align:center;color:var(--label);font-weight:600;font-size:68px;letter-spacing:12px}

/* Cards */
.card{left:217px;width:767px;height:438px}
.card-front{top:1758px}
.card-back{top:2319px}
.card-front .brand{left:0;width:767px;justify-content:center;top:140px;font-size:54px}
.card-front .brand-mark{width:58px;height:58px}
.card-front .url{left:0;width:767px;top:282px;text-align:center;font-size:30px;letter-spacing:9px}
.card-front .url b{color:var(--orange);font-weight:700}
.card-back .brand{left:36px;top:196px;font-size:38px}
.card-back .brand-mark{width:44px;height:44px}
.holder{left:447px;top:104px}
.holder .name{font-size:29px;font-weight:700;color:var(--navy);line-height:40px}
.holder .role{font-size:18px;line-height:28px}
.card-details{left:447px;top:190px;display:flex;gap:14px}
.card-details .bar{width:30px;height:140px;background:var(--navy);border-radius:15px;display:flex;flex-direction:column;justify-content:space-around;align-items:center;padding:4px 0}
.card-details .vals{font-size:14.5px;line-height:17px;display:flex;flex-direction:column;justify-content:space-between;padding:2px 0}
</style>
</head>
<body>
<div class="canvas">

  <section class="sheet letterhead">
    <svg class="decor" width="941" height="1330" viewBox="0 0 941 1330">
      <defs>
        <linearGradient id="warm" x1="0" y1="1" x2="1" y2="0">
          <stop offset="0" stop-color="#e8200f"/><stop offset="1" stop-color="#ff7a00"/>
        </linearGradient>
        <linearGradient id="cool" x1="0" y1="1" x2="1" y2="0">
          <stop offset="0" stop-color="#0d3789"/><stop offset="1" stop-color="#0a6fc0"/>
        </linearGradient>
        <linearGradient id="rule" x1="0" x2="1">
          <stop offset="0" stop-color="#ffa000"/><stop offset="1" stop-color="#f05a0a"/>
        </linearGradient>
      </defs>
      <line x1="330" y1="133" x2="420" y2="133" stroke="#f57c00" stroke-width="1.5"/>
      <polygon points="420,134 432,120 941,120 941,134" fill="url(#rule)"/>
      <polygon points="941,1045 941,1095 810,1330 754,1330" fill="url(#cool)"/>
      <polygon points="941,1125 941,1330 820,1330" fill="url(#warm)"/>
      <rect x="0" y="1324" width="600" height="6" fill="var(--blue)"/>
      <polygon points="585,1330 600,1316 941,1316 941,1330" fill="url(#warm)"/>
    </svg>

    <div class="abs brand"><i class="brand-mark"></i>VELTRONA</div>

    <div class="abs recipient">
      <div class="to">To</div>
      <div class="name">Dr. Adrian le Roux</div>
      <div class="role">Founder &amp; Lead Researcher</div>
    </div>

    <div class="abs contact-box">
      <div class="keys"><span>P</span><span>A</span><span>W</span></div>
      <div class="vals">
        <span>+0000 987 654 32</span>
        <span>Headquarters in Malta, with<br>presence across EMEA &amp; US</span>
        <span>www.veltrona.com</span>
      </div>
    </div>

    <div class="abs subject"><b>Subject:</b> Lorem ipsum dolor sit amet, consectetur adipisicing elit,</div>

    <div class="abs body">
      <p>Lorem ipsum dolor sit amet, consectetur adipiscing elit. Donec vitae turpis suscipit, elementun ligula vestibulum, luctus velit. Quisque dui purus, venenatis dictum lorem vitae, elementum bibendum felis. Praesent sodales eleifend lacinia. Praesent non molestie velit. Mauris congue justo elernentum enim mollis, et pharetra sem ultrices. Mauris molestie, tellus at convallis condimentum, enim diam porta nisl, nec aliquam quam augue dapibus eros. Cras volutpat sollicitudin mauris quis ultricies. Curabitur lacinia vitae massa in molestie. Aenean vulputate accumsan lectus en egestas.</p>
      <p>Cras nec ipsum magna. In tincidunt sem tellus. Aliquam erat volutpat. In hac habitasse platea dictumst. Donec cursus lectus sed urna gravida gravida. Suspendisse eu tellus at urna fringilla tincidunt nec sit amet lorem. Nam ac vestibulum velit. Donec sodales sem eget erat dignissim semper. Phasellus faucibus, dolor at condimentum imperdiet, dolor sapien interdum ante, et posuere arcu ipsum ut nisi. Sed condimentum hendrerit ante vel maximus. Maecenas faucibus est vel odio maximus auctor. Integer eu lectus nec purus elementum mollis. Aenean eu nisl sit amet risus fermentum efficitur vestibulum eu est. Sed semper metus vel arcu blandit finibus. Fusce mollis neque ac justo efficitur, et egestas libero auctor.</p>
      <p>Nunc maximus risus vel arcu mattis facilisis. Integer euismod euismod convallis. Suspendisse ac rutrum lectus. Quisque pharetra sapien nibh. Mauris porttitor<br>tellus nec velit hendrerit accumsan.</p>
    </div>

    <div class="abs signoff">
      <div class="script">Yours Sincerely</div>
      <div class="name">Peter Hallam</div>
      <div class="role">Manager</div>
    </div>
    <div class="abs date">23.07.2026</div>

    <div class="abs contact-row">
      <span><i class="icon"><svg width="16" height="16" viewBox="0 0 24 24"><path fill="#fff" d="M6.6 10.8a15 15 0 0 0 6.6 6.6l2.2-2.2c.3-.3.7-.4 1-.2 1.1.4 2.3.6 3.6.6.6 0 1 .4 1 1V20c0 .6-.4 1-1 1A17 17 0 0 1 3 4c0-.6.4-1 1-1h3.5c.6 0 1 .4 1 1 0 1.3.2 2.5.6 3.6.1.3 0 .7-.2 1z"/></svg></i>+01-5555-6666-7777</span>
      <span><i class="icon"><svg width="16" height="16" viewBox="0 0 24 24"><rect x="3" y="6" width="18" height="12" rx="1" fill="none" stroke="#fff" stroke-width="2"/><path d="M3 7l9 6 9-6" fill="none" stroke="#fff" stroke-width="2"/></svg></i>info@peterhallam.com</span>
      <span><i class="icon"><svg width="16" height="16" viewBox="0 0 24 24"><circle cx="12" cy="12" r="9" fill="none" stroke="#fff" stroke-width="2"/><path d="M3 12h18M12 3c3 3 3 15 0 18M12 3c-3 3-3 15 0 18" fill="none" stroke="#fff" stroke-width="1.6"/></svg></i>www.peterhallam.com</span>
    </div>
  </section>

  <div class="label" style="top:1548px">LETTERHEAD</div>

  <section class="card card-front">
    <svg class="decor" width="767" height="438" viewBox="0 0 767 438">
      <defs>
        <linearGradient id="warm2" x1="0" y1="1" x2="1" y2="0">
          <stop offset="0" stop-color="#e8200f"/><stop offset="1" stop-color="#ff7a00"/>
        </linearGradient>
      </defs>
      <polygon points="0,345 0,380 70,438 112,438" fill="var(--navy)"/>
      <polygon points="0,398 0,438 40,438" fill="var(--orange)"/>
      <polygon points="72,420 245,420 258,438 86,438" fill="var(--navy)"/>
      <polygon points="767,300 767,438 668,438" fill="url(#warm2)"/>
      <polygon points="520,438 532,428 690,428 682,438" fill="var(--red)"/>
    </svg>
    <div class="abs brand"><i class="brand-mark"></i>VELTRONA</div>
    <div class="abs url">www.<b>veltrona</b>.com</div>
  </section>

  <section class="card card-back">
    <svg class="decor" width="767" height="438" viewBox="0 0 767 438">
      <defs>
        <linearGradient id="warm3" x1="0" y1="1" x2="1" y2="0">
          <stop offset="0" stop-color="#e8200f"/><stop offset="1" stop-color="#ff7a00"/>
        </linearGradient>
      </defs>
      <polygon points="0,345 0,380 70,438 112,438" fill="var(--navy)"/>
      <polygon points="0,398 0,438 40,438" fill="var(--orange)"/>
      <polygon points="72,420 245,420 258,438 86,438" fill="var(--navy)"/>
      <polygon points="767,300 767,438 668,438" fill="url(#warm3)"/>
      <polygon points="520,438 532,428 690,428 682,438" fill="var(--red)"/>
    </svg>
    <div class="abs brand"><i class="brand-mark"></i>VELTRONA</div>
    <div class="abs holder">
      <div class="name">Dr. Adrian le Roux</div>
      <div class="role">Founder &amp; Lead Researcher</div>
    </div>
    <div class="abs card-details">
      <div class="bar">
        <svg width="15" height="15" viewBox="0 0 24 24"><path fill="#fff" d="M6.6 10.8a15 15 0 0 0 6.6 6.6l2.2-2.2c.3-.3.7-.4 1-.2 1.1.4 2.3.6 3.6.6.6 0 1 .4 1 1V20c0 .6-.4 1-1 1A17 17 0 0 1 3 4c0-.6.4-1 1-1h3.5c.6 0 1 .4 1 1 0 1.3.2 2.5.6 3.6.1.3 0 .7-.2 1z"/></svg>
        <svg width="15" height="15" viewBox="0 0 24 24"><rect x="3" y="6" width="18" height="12" rx="1" fill="none" stroke="#fff" stroke-width="2"/><path d="M3 7l9 6 9-6" fill="none" stroke="#fff" stroke-width="2"/></svg>
        <svg width="15" height="15" viewBox="0 0 24 24"><path fill="#fff" d="M12 2a7 7 0 0 0-7 7c0 5 7 13 7 13s7-8 7-13a7 7 0 0 0-7-7zm0 9.5A2.5 2.5 0 1 1 12 6.5a2.5 2.5 0 0 1 0 5z"/></svg>
        <svg width="15" height="15" viewBox="0 0 24 24"><circle cx="12" cy="12" r="9" fill="none" stroke="#fff" stroke-width="2"/><path d="M3 12h18M12 3c3 3 3 15 0 18M12 3c-3 3-3 15 0 18" fill="none" stroke="#fff" stroke-width="1.6"/></svg>
      </div>
      <div class="vals">
        <span>+0000 987 654 32</span>
        <span>Info@veltrona.com</span>
        <span>Headquarters in Malta, with<br>presence across EMEA &amp; US</span>
        <span>www.veltrona.com</span>
      </div>
    </div>
  </section>

  <div class="label" style="top:2860px">BUSINESS CARD</div>

</div>
</body>
</html>
```